Figure for Manufacture of Wound Healing Gel

Who we are: We are a nationally funded bioengineering laboratory at Harlow Ridge University conducting research on the tendon healing properties of a gel manufactured from real tendon.

What we need: We require a figure piece that will be included in an academic publication. With that in mind, the figure must be professional, clear, and concise. A reader would need to glance at the figure for only a moment to understand the process of how we manufacture and store tendon gel. Actual pictures of the in-between steps are included and will need to be cropped to improve the professional look of the design.

The Details: The figure should stepwise show the process of how we manufacture and store tendon gel. In brief, we harvest tendon from donor cadavers. Those tendons undergo decellularization, lyophilization (fancy word for freeze-drying), and are milled into a fine powder. The powder is set in acidified water and treated with digestive enzymes. After 24 hrs, the gel is brought to physiologic pH and salinity and placed in vials. The vials are frozen and again lyophilized (this is so they can be stored and transported easily). Finally the samples are reconstituted with DI water.

The Figure: Should be a linear process (horizontal). The following are the actual steps we wish to include (steps need not be numbered necessarily as long as they are in logical order...

1.) A picture of harvested tendon (Step 1.jpg)
2.) Written description: "Decellularization, lyophilization, and milling"
3.) A picture of milled tendon powder (Step 2.jpg)
4.) Written description: "Digestion with pepsin before establishing physiologic pH and salinity".
5.) A picture of gel (Step 3.jpg)
6.) Written description: "Lyophilization of aliquots"
7.) A picture of freeze-dried gel (Step 4.jpg)
8.) Written description: "Reconstitution with DI water"
9.) A picture of reconstituted gel (Step 5.jpg)

Feel free to message for any questions, comments, or clarifications.

```html
<!DOCTYPE html>
<html lang="en">
<head>
<meta charset="utf-8">
<title>Manufacture of Wound Healing Gel</title>
<link rel="stylesheet" href="https://fonts.googleapis.com/css2?family=Caladea&display=swap">
<style>
  :root {
    --paper: #ffffff;
    --ink: #111111;
    --arrow-dark: #111111;
    --arrow-grey: #7a7a7a;
    --dish-edge: #9a9a9a;
    --dish-glass: #d9dadb;
    --tendon: #e6dcc6;
    --powder: #efe6c8;
    --gel: #f1eee8;
    --cap: #e8542a;
    --tube: #dcdfe2;
    --gel-dry: #e8dcc3;
    --gel-wet: #e3dcc6;
  }
  * { margin: 0; padding: 0; box-sizing: border-box; }
  html, body { width: 1200px; height: 900px; overflow: hidden; background: var(--paper); }
  .canvas { position: relative; width: 1200px; height: 900px; font-family: "Caladea", "Cambria", Georgia, serif; color: var(--ink); }
  .option-title { position: absolute; left: 33px; font-size: 38px; font-weight: 400; letter-spacing: 1px; line-height: 1; }
  .option-title.first { top: 64px; }
  .option-title.second { top: 498px; }
  .photo { position: absolute; }
  .dish { border-radius: 50%; border: 2px solid var(--dish-edge); background: radial-gradient(ellipse at center, var(--fill) 0 38%, var(--dish-glass) 62%, #f4f4f4 100%); }
  .dish.tendon { --fill: var(--tendon); }
  .dish.powder { --fill: var(--powder); }
  .dish.gel { --fill: var(--gel); }
  .vial { border-radius: 4px 4px 10px 10px; background: linear-gradient(to bottom, var(--cap) 0 24%, var(--tube) 24% 55%, var(--vialfill) 55% 100%); }
  .vial.dry { --vialfill: var(--gel-dry); }
  .vial.wet { --vialfill: var(--gel-wet); }
  .step-label { position: absolute; text-align: center; line-height: 1.45; }
  .row-compact .step-label { font-size: 9px; }
  .row-spaced .step-label { font-size: 12.5px; line-height: 1.6; }
  svg.arrows { position: absolute; left: 0; top: 0; width: 1200px; height: 900px; }
</style>
</head>
<body>
<div class="canvas">
  <h2 class="option-title first">OPTION 1</h2>

  <section class="row-compact">
    <div class="photo dish tendon" style="left:6px;top:196px;width:114px;height:68px" role="img" aria-label="Photo of harvested tendon in a glass dish"></div>
    <p class="step-label" style="left:170px;top:213px;width:120px">Decellularization, lyophilization, and milling</p>
    <div class="photo dish powder" style="left:329px;top:196px;width:104px;height:68px" role="img" aria-label="Photo of milled tendon powder in a glass dish"></div>
    <p class="step-label" style="left:474px;top:204px;width:90px">Digestion with pepsin before establishing physiologic pH and salinity</p>
    <div class="photo dish gel" style="left:602px;top:196px;width:91px;height:68px" role="img" aria-label="Photo of digested tendon gel in a glass dish"></div>
    <p class="step-label" style="left:740px;top:204px;width:120px">Lyophilization of aliquots Reconstitution with DI water Completed process - reconstituted gel</p>
    <div class="photo vial dry" style="left:913px;top:186px;width:30px;height:86px" role="img" aria-label="Photo of freeze-dried gel in a capped vial"></div>
    <p class="step-label" style="left:984px;top:217px;width:94px">Reconstitution with DI water</p>
    <div class="photo vial wet" style="left:1130px;top:183px;width:30px;height:89px" role="img" aria-label="Photo of reconstituted gel in a capped vial"></div>
  </section>

  <h2 class="option-title second">OPTION 2</h2>

  <section class="row-spaced">
    <div class="photo dish tendon" style="left:18px;top:630px;width:130px;height:88px" role="img" aria-label="Photo of harvested tendon in a glass dish"></div>
    <p class="step-label" style="left:150px;top:742px;width:176px">Decellularization, lyophilization, and milling</p>
    <div class="photo dish powder" style="left:283px;top:628px;width:127px;height:90px" role="img" aria-label="Photo of milled tendon powder in a glass dish"></div>
    <p class="step-label" style="left:435px;top:740px;width:130px">Digestion with pepsin before establishing physiologic pH and salinity</p>
    <div class="photo dish gel" style="left:591px;top:628px;width:102px;height:90px" role="img" aria-label="Photo of digested tendon gel in a glass dish"></div>
    <p class="step-label" style="left:718px;top:742px;width:166px">Lyophilization of aliquots Reconstitution with DI water Completed process - reconstituted gel</p>
    <div class="photo vial dry" style="left:903px;top:600px;width:38px;height:124px" role="img" aria-label="Photo of freeze-dried gel in a capped vial"></div>
    <p class="step-label" style="left:976px;top:742px;width:130px">Reconstitution with DI water</p>
    <div class="photo vial wet" style="left:1131px;top:597px;width:41px;height:127px" role="img" aria-label="Photo of reconstituted gel in a capped vial"></div>
  </section>

  <svg class="arrows" viewBox="0 0 1200 900" aria-hidden="true">
    <defs>
      <marker id="head-dark" viewBox="0 0 10 10" refX="9" refY="5" markerWidth="6" markerHeight="6" orient="auto"><path d="M0 0 L10 5 L0 10 Z" fill="var(--arrow-dark)"/></marker>
      <marker id="head-grey" viewBox="0 0 10 10" refX="9" refY="5" markerWidth="5" markerHeight="5" orient="auto"><path d="M0 0 L10 5 L0 10 Z" fill="var(--arrow-grey)"/></marker>
    </defs>
    <g stroke="var(--arrow-dark)" stroke-width="2" marker-end="url(#head-dark)">
      <line x1="128" y1="230" x2="163" y2="230"/>
      <line x1="283" y1="230" x2="318" y2="230"/>
      <line x1="437" y1="230" x2="472" y2="230"/>
      <line x1="563" y1="230" x2="598" y2="230"/>
      <line x1="703" y1="230" x2="738" y2="230"/>
      <line x1="858" y1="230" x2="893" y2="230"/>
      <line x1="946" y1="230" x2="981" y2="230"/>
      <line x1="1082" y1="230" x2="1117" y2="230"/>
    </g>
    <g stroke="var(--arrow-grey)" stroke-width="2.5" marker-end="url(#head-grey)">
      <line x1="137" y1="716" x2="162" y2="740"/>
      <line x1="265" y1="740" x2="291" y2="707"/>
      <line x1="411" y1="711" x2="436" y2="736"/>
      <line x1="570" y1="738" x2="595" y2="707"/>
      <line x1="705" y1="711" x2="730" y2="736"/>
      <line x1="867" y1="735" x2="893" y2="705"/>
      <line x1="948" y1="711" x2="973" y2="738"/>
      <line x1="1100" y1="740" x2="1126" y2="710"/>
    </g>
  </svg>
</div>
</body>
</html>
```